360degree attack angle on military vehicle

I need a grahical design/picture, that shows a military vehicle is protected against bullets 360degree around the vehicle and from 0-30degree in elevation.
It needs to have a technical expression, because it will be used by engineers to present the protection of our products.

I have attached a picture that can be used for inspiration.
If a vehicle could be placed in the circle, and the same vehicle transparent rotated around the center. (like the shoe in the picture, but seen from an angle above like the sketch indicates)

Requirements
Must have
• military vehicle

```html
<!DOCTYPE html>
<html lang="en">
<head>
<meta charset="utf-8">
<title>360° Azimuth Protection Diagram</title>
<link rel="stylesheet" href="https://fonts.googleapis.com/css2?family=Oswald:wght@600&family=Orbitron:wght@600;800&display=swap">
<style>
  :root {
    --navy: #14309a;
    --navy-deep: #222d62;
    --sky: #18aaf5;
    --sky-pale: #bfe6fd;
    --dome: #8fcdfb;
    --ring: #10a6f6;
    --frontal: #e0485f;
    --elev: #12dcc0;
    --bg: #ffffff;
  }
  html, body {
    margin: 0;
    padding: 0;
    width: 1200px;
    height: 865px;
    overflow: hidden;
    background: var(--bg);
  }
  .diagram {
    display: block;
    width: 1200px;
    height: 865px;
  }
  .degree-label {
    font-family: "Oswald", sans-serif;
    font-weight: 600;
    font-size: 22px;
    fill: var(--navy);
    letter-spacing: 1px;
  }
  .axis-label {
    font-family: "Orbitron", sans-serif;
    font-weight: 600;
    font-size: 17px;
    fill: var(--navy);
  }
  .azimuth-title {
    font-family: "Orbitron", sans-serif;
    font-weight: 800;
    font-size: 58px;
    fill: var(--sky);
    letter-spacing: 10px;
  }
</style>
</head>
<body>
<svg class="diagram" viewBox="0 0 1200 865" xmlns="http://www.w3.org/2000/svg">
  <defs>
    <radialGradient id="ground-fill" cx="50%" cy="50%" r="50%">
      <stop offset="0" stop-color="#1aa4ff"/>
      <stop offset="0.55" stop-color="#2fb6fb"/>
      <stop offset="1" stop-color="#d7effd"/>
    </radialGradient>
    <linearGradient id="dome-fill" x1="0" y1="0" x2="0" y2="1">
      <stop offset="0" stop-color="#86c9fb" stop-opacity="0.95"/>
      <stop offset="0.5" stop-color="#c6e4fb" stop-opacity="0.75"/>
      <stop offset="1" stop-color="#dceefc" stop-opacity="0.6"/>
    </linearGradient>
    <linearGradient id="frontal-fill" x1="0" y1="0" x2="0" y2="1">
      <stop offset="0" stop-color="#e2405a"/>
      <stop offset="1" stop-color="#c7b4e6" stop-opacity="0.8"/>
    </linearGradient>
    <linearGradient id="elevation-fill" x1="0" y1="0" x2="1" y2="0">
      <stop offset="0" stop-color="#0bd8c8"/>
      <stop offset="1" stop-color="#8fe9a8" stop-opacity="0.7"/>
    </linearGradient>
    <linearGradient id="arrow-fill" x1="0" y1="0" x2="0" y2="1">
      <stop offset="0" stop-color="#9fd6fb"/>
      <stop offset="1" stop-color="#2aa6f7"/>
    </linearGradient>
    <marker id="arrow-head" viewBox="0 0 10 10" refX="5" refY="5" markerWidth="3" markerHeight="3" orient="auto-start-reverse">
      <path d="M0 0 L10 5 L0 10 Z" fill="#4ab6f8"/>
    </marker>
    <path id="azimuth-path" d="M 128 470 A 475 258 0 0 0 1078 470"/>
  </defs>

  <!-- outer dotted halo rings -->
  <g class="halo-rings" fill="none" stroke="var(--sky-pale)" stroke-linecap="round" stroke-dasharray="0 7">
    <ellipse cx="603" cy="475" rx="420" ry="205" stroke-width="4"/>
    <ellipse cx="603" cy="478" rx="445" ry="222" stroke-width="4"/>
    <ellipse cx="603" cy="481" rx="470" ry="240" stroke-width="4"/>
    <ellipse cx="603" cy="484" rx="495" ry="258" stroke-width="3.5"/>
    <ellipse cx="603" cy="488" rx="520" ry="276" stroke-width="3"/>
  </g>

  <!-- rotation arrows -->
  <g class="rotation-arrows" fill="none" stroke="url(#arrow-fill)" stroke-width="20" opacity="0.85">
    <path d="M 215 362 Q 140 400 150 488" marker-start="url(#arrow-head)" marker-end="url(#arrow-head)"/>
    <path d="M 995 362 Q 1070 400 1060 488" marker-start="url(#arrow-head)" marker-end="url(#arrow-head)"/>
  </g>

  <!-- ground disc -->
  <ellipse class="ground-disc" cx="603" cy="470" rx="372" ry="170" fill="url(#ground-fill)"/>
  <g class="range-rings" fill="none" stroke="#2a48d8" stroke-width="1.2" stroke-dasharray="5 4">
    <ellipse cx="600" cy="455" rx="318" ry="148"/>
    <ellipse cx="600" cy="452" rx="265" ry="122"/>
    <ellipse cx="600" cy="450" rx="212" ry="97"/>
    <ellipse cx="600" cy="448" rx="160" ry="72"/>
    <ellipse cx="600" cy="446" rx="110" ry="48"/>
  </g>

  <!-- frontal arc -->
  <path class="frontal-arc" d="M 600 457 L 337 580 A 300 60 0 0 0 868 580 Z" fill="url(#frontal-fill)" opacity="0.9"/>
  <g class="frontal-scale" fill="none" stroke="var(--navy)" stroke-width="1.3">
    <line x1="600" y1="457" x2="337" y2="580"/>
    <line x1="600" y1="457" x2="868" y2="580"/>
    <path d="M 348 584 Q 600 690 855 587"/>
    <g stroke-width="1">
      <line x1="378" y1="596" x2="380" y2="590"/>
      <line x1="418" y1="608" x2="421" y2="598"/>
      <line x1="458" y1="617" x2="460" y2="610"/>
      <line x1="495" y1="624" x2="497" y2="614"/>
      <line x1="540" y1="630" x2="541" y2="623"/>
      <line x1="599" y1="636" x2="599" y2="621"/>
      <line x1="655" y1="630" x2="654" y2="623"/>
      <line x1="700" y1="625" x2="699" y2="615"/>
      <line x1="740" y1="617" x2="738" y2="610"/>
      <line x1="780" y1="609" x2="777" y2="599"/>
      <line x1="820" y1="598" x2="818" y2="592"/>
    </g>
  </g>

  <!-- main azimuth ring -->
  <ellipse class="azimuth-ring" cx="603" cy="472" rx="382" ry="178" fill="none" stroke="var(--ring)" stroke-width="9"/>
  <ellipse class="azimuth-ring-thin" cx="603" cy="472" rx="398" ry="192" fill="none" stroke="var(--ring)" stroke-width="1.5"/>

  <!-- protection dome -->
  <path class="dome" d="M 260 470 A 345 356 0 0 1 950 470 A 345 130 0 0 1 260 470 Z" fill="url(#dome-fill)" opacity="0.8"/>
  <ellipse class="dome-latitude" cx="605" cy="279" rx="295" ry="109" fill="none" stroke="var(--navy)" stroke-width="2" stroke-dasharray="0 6" stroke-linecap="round"/>

  <!-- elevation sector -->
  <path class="elevation-sector" d="M 605 431 L 903 262 A 350 325 0 0 1 955 431 Z" fill="url(#elevation-fill)" opacity="0.85"/>
  <g class="elevation-scale" fill="none" stroke="var(--navy)" stroke-width="1.4">
    <line x1="605" y1="431" x2="956" y2="431"/>
    <line x1="605" y1="431" x2="903" y2="260"/>
    <line x1="605" y1="365" x2="608" y2="106"/>
    <path d="M 608 106 A 350 325 0 0 1 956 431"/>
    <line x1="608" y1="106" x2="608" y2="98"/>
    <line x1="956" y1="431" x2="956" y2="423"/>
    <g stroke-width="1">
      <line x1="668" y1="111" x2="667" y2="119"/>
      <line x1="727" y1="126" x2="724" y2="133"/>
      <line x1="782" y1="150" x2="777" y2="157"/>
      <line x1="831" y1="184" x2="825" y2="190"/>
      <line x1="872" y1="225" x2="865" y2="230"/>
      <line x1="927" y1="310" x2="919" y2="313"/>
      <line x1="946" y1="356" x2="938" y2="358"/>
      <line x1="954" y1="395" x2="946" y2="396"/>
    </g>
  </g>

  <!-- vehicle -->
  <path class="vehicle" role="img" aria-label="Front-top technical line drawing of an armoured tracked vehicle with turret and cannon"
        d="M 517 332 L 680 332 L 703 470 L 727 528 L 727 553 L 473 553 L 473 528 L 497 470 Z"
        fill="var(--navy-deep)"/>

  <!-- labels -->
  <text class="degree-label" x="613" y="98" text-anchor="middle">90°</text>
  <text class="degree-label" x="920" y="258" text-anchor="middle">30°</text>
  <text class="degree-label" x="985" y="430" text-anchor="middle">0°</text>
  <text class="degree-label" x="325" y="576" text-anchor="middle">30°</text>
  <text class="degree-label" x="883" y="576" text-anchor="middle">30°</text>
  <text class="degree-label" x="603" y="664" text-anchor="middle">0°</text>
  <text class="axis-label" x="1001" y="299" text-anchor="middle">ELEVATION</text>
  <text class="axis-label" x="598" y="599" text-anchor="middle">FRONTAL ARC</text>

  <text class="azimuth-title">
    <textPath href="#azimuth-path" startOffset="50%" text-anchor="middle">360° AZIMUTH</textPath>
  </text>
</svg>
</body>
</html>
```